Brand Identity Redesign for Harbourline Painting - DELIVERABLE - Brand Guide Poster

DELIVERABLE - Brand Guide Poster (see attached Brand Guide Poster 1 and Brand Guide example 2).
- We are seeking graphic designers who can help us reimagine and revamp our brand identity based on our new Harbourline Painting logo. We are looking for a fresh and modern approach that aligns with our values and attracts our target audience.
- The task involves creating a comprehensive brand identity system that includes:
- Logo variations and usage guidelines
- Colour palette selection and guidelines
- Typography selection and guidelines
- Graphic elements, patterns, or textures
- Visual style guidelines for various applications (e.g., website, social media, marketing materials - online and offline)
- Brand collateral design (business cards, letterheads, brochures, quotes, invoices, proposals, vehicle signage, yard signage, worksite signage, etc.)
- The designer should have experience in brand identity design and a strong portfolio showcasing their skills in creating visually appealing and cohesive brand identities.
- The project will require collaboration, as we will provide our new logo and any specific design preferences, and expect the designer to incorporate these elements while offering their creative expertise.
- The deliverables should be provided in digital formats (e.g., vector files, design software files) and accompanied by a brand guidelines document explaining the proper usage of the brand identity elements. See attached example of brand guidelines poster. A one page guide like this would be awesome.

Target Market(s)

1. Wealthy Home Owners with a primary residence and holiday homes on the Central Coast of NSW Overview: Harbourline Painting works extensively with wealthy home owners on the Central Coast of NSW who own beachside properties. These customers typically require extensive maintenance and protection from corrosion due to the harsh coastal environment. 2. Companies who manage multiple properties in New South Wales.

Industry/Entity Type

Painting and decorating

Font styles to use
Serif
Sans Serif

Requirements
Must have
• Overall style should exude sophistication, professionalism, and attention to detail. The design should convey a sense of craftsmanship and longevity, emphasizing the company's focus on protecting surfaces for long-lasting durability. The logo should be sleek, clean, and modern, while still maintaining a classic and timeless feel. It should be versatile and scalable to ensure it can be used across various marketing materials. Brand guidelines poster - see attached example.
Should not have
• Very bright colours that look cheap. I have attached some logos that will be displayed on all our marketing along with a colour scheme that complements them and the logo. I am, however, very open to suggestions.

```html
<!DOCTYPE html>
<html lang="en">
<head>
<meta charset="utf-8">
<title>Harbourline Painting – Brand Guidelines 2023</title>
<link rel="stylesheet" href="https://fonts.googleapis.com/css2?family=Cinzel:wght@400&family=Nunito+Sans:wght@400;600&family=Open+Sans:wght@400;700&display=swap">
<style>
  :root {
    --navy: #022859;
    --sky: #04B1D9;
    --charcoal: #3F3F3F;
    --grey: #A6A6A6;
    --silver: #D8D8D6;
    --paper: #EFF4F4;
    --white: #FFFFFF;
    --ink: #000000;
  }
  * { margin: 0; padding: 0; box-sizing: border-box; }
  html, body { width: 1200px; height: 2400px; overflow: hidden; background: var(--white); }
  .poster { position: relative; width: 1200px; height: 2400px; font-family: "Open Sans", sans-serif; color: var(--ink); }
  .abs { position: absolute; }

  .doc-title { left: 55px; top: 38px; font-size: 46px; letter-spacing: 15px; color: var(--grey); font-weight: 400; }
  .doc-year { right: 50px; top: 38px; font-size: 46px; letter-spacing: 12px; color: var(--grey); font-weight: 400; }

  .brand-name { font-family: "Nunito Sans", sans-serif; font-weight: 600; white-space: nowrap; line-height: 1; }

  .hero-name { left: 0; width: 1200px; top: 200px; text-align: center; font-size: 74px; color: var(--ink); }

  .section-title { font-size: 37px; font-weight: 700; color: var(--grey); }

  .variant { display: flex; align-items: center; justify-content: center; }
  .variant .brand-name { font-size: 33px; }
  .v-navy { color: var(--navy); }
  .v-charcoal { color: var(--charcoal); }
  .v-on-sky { background: var(--sky); color: var(--white); }
  .v-on-navy { background: var(--navy); color: var(--white); }

  .type-band { left: 0; top: 767px; width: 1200px; height: 325px; background: var(--navy); color: var(--white); }
  .type-band .section-title { color: var(--white); left: 44px; top: 14px; font-size: 39px; }
  .type-label { font-size: 28px; }
  .font-name { font-size: 30px; }
  .licence { font-size: 20px; }
  .cinzel { font-family: "Cinzel", serif; }
  .nunito { font-family: "Nunito Sans", sans-serif; }
  .sample { font-size: 28px; left: 335px; }

  .palette-label { font-size: 28px; }
  .swatch { width: 152px; height: 262px; top: 1230px; }
  .spec { top: 1520px; font-size: 17px; line-height: 23px; }

  .card { width: 310px; height: 178px; left: 194px; }
  .card-front { top: 1743px; background: var(--paper); color: var(--navy); text-align: center; }
  .card-front .person { font-family: "Cinzel", serif; font-size: 27px; margin-top: 50px; }
  .card-front .role { font-family: "Cinzel", serif; font-size: 17px; }
  .card-front .contact { font-size: 7.5px; position: absolute; top: 150px; }
  .card-front .address { font-size: 7.5px; position: absolute; top: 165px; width: 100%; }
  .card-back { top: 1955px; background: var(--navy); color: var(--white); display: flex; align-items: center; justify-content: center; border-bottom: 5px solid var(--sky); }
  .card-back .brand-name { font-size: 24px; }

  .letterhead { left: 527px; top: 1743px; width: 432px; height: 391px; background: var(--paper); }
  .letterhead .head { height: 98px; background: var(--navy); border-bottom: 5px solid var(--sky); color: var(--white); padding: 34px 0 0 18px; }
  .letterhead .head .brand-name { font-size: 20px; }
  .letterhead .foot { position: absolute; bottom: 10px; width: 100%; text-align: center; font-size: 6.5px; color: var(--navy); }

  .icon-band { left: 0; top: 2178px; width: 1200px; height: 222px; background: var(--navy); }
  .icon-band .section-title { color: var(--white); left: 74px; top: 18px; }
  .icon-row { left: 0; top: 0; }
  .icons-white { color: var(--white); }
  .icons-sky { color: var(--sky); }
</style>
</head>
<body>
<main class="poster">
  <h1 class="abs doc-title">BRAND GUIDELINES</h1>
  <div class="abs doc-year">2023</div>

  <div class="abs brand-name hero-name">Harbourline Painting</div>

  <h2 class="abs section-title" style="left:44px;top:385px;">LOGO VARIATIONS</h2>
  <div class="abs variant v-navy" style="left:155px;top:460px;width:404px;height:90px;">
    <span class="brand-name">Harbourline Painting</span>
  </div>
  <div class="abs variant v-charcoal" style="left:641px;top:460px;width:405px;height:90px;">
    <span class="brand-name">Harbourline Painting</span>
  </div>
  <div class="abs variant v-on-sky" style="left:155px;top:587px;width:404px;height:138px;">
    <span class="brand-name">Harbourline Painting</span>
  </div>
  <div class="abs variant v-on-navy" style="left:641px;top:593px;width:405px;height:137px;">
    <span class="brand-name">Harbourline Painting</span>
  </div>

  <section class="abs type-band">
    <h2 class="abs section-title">CORPORATE TYPOGRAPHY</h2>
    <div class="abs type-label" style="left:38px;top:60px;">FONT:</div>
    <div class="abs font-name cinzel" style="left:38px;top:112px;">CINZEL</div>
    <div class="abs licence" style="left:38px;top:150px;">Standard CC0 font license</div>
    <div class="abs sample cinzel" style="top:104px;">ABCDEFGHIJKLMNOPQRSTUVWXYZ</div>
    <div class="abs sample cinzel" style="top:146px;font-size:26px;">ABCDEFGHIJKLMNOPQRSTUVWXYZ</div>
    <div class="abs font-name nunito" style="left:38px;top:233px;">Nunito Sans</div>
    <div class="abs licence" style="left:38px;top:270px;">Standard CC0 font license</div>
    <div class="abs sample nunito" style="top:222px;">ABCDEFGHIJKLMNOPQRSTUVWXYZ</div>
    <div class="abs sample nunito" style="top:265px;">abcdefghijklmnopqrstuvwxyz</div>
  </section>

  <h2 class="abs section-title" style="left:44px;top:1122px;">CORPORATE COLORS</h2>
  <div class="abs palette-label" style="left:38px;top:1188px;">PRIMARY COLORS:</div>
  <div class="abs palette-label" style="left:729px;top:1188px;">SECONDARY COLORS:</div>

  <div class="abs swatch" style="left:48px;background:var(--navy);"></div>
  <div class="abs swatch" style="left:232px;background:var(--sky);"></div>
  <div class="abs swatch" style="left:416px;background:var(--charcoal);"></div>
  <div class="abs swatch" style="left:741px;background:var(--grey);"></div>
  <div class="abs swatch" style="left:919px;background:var(--silver);"></div>

  <div class="abs spec" style="left:48px;">#022859<br>RGB: 2,40,89<br>CMYK: 100,87,32,42<br>Pantone 534 C</div>
  <div class="abs spec" style="left:232px;">#04B1D9<br>RGB: 4,177,217<br>CMYK: 100,7,17,0<br>Pantone 312 C</div>
  <div class="abs spec" style="left:416px;">#3F3F3F<br>RGB: 63,63,63<br>CMYK: 67,60,59,46<br>Pantone 446 C</div>
  <div class="abs spec" style="left:741px;">#A6A6A6<br>RGB: 166,166,166<br>CMYK: 38,31,31,0<br>Pantone 443 C</div>
  <div class="abs spec" style="left:919px;">#D8D8D6<br>RGB: 216,216,214<br>CMYK: 15,11,13,0<br>Pantone 427 C</div>

  <h2 class="abs section-title" style="left:66px;top:1644px;">CORPORATRE STATIONARY</h2>

  <div class="abs card card-front">
    <div class="person">Leon Marsh</div>
    <div class="role">CEO</div>
    <svg class="abs" style="left:85px;top:130px;" width="14" height="14" viewBox="0 0 14 14" aria-hidden="true"><circle cx="7" cy="7" r="6" fill="none" stroke="var(--navy)" stroke-width="1"/><path d="M4.5 4.5c0 3 2 5 5 5l.6-1.3-1.4-.7-.7.7c-1-.4-1.8-1.2-2.2-2.2l.7-.7-.7-1.4z" fill="var(--navy)"/></svg>
    <svg class="abs" style="left:236px;top:130px;" width="14" height="14" viewBox="0 0 14 14" aria-hidden="true"><circle cx="7" cy="7" r="6" fill="none" stroke="var(--navy)" stroke-width="1"/><rect x="4" y="5" width="6" height="4.2" fill="none" stroke="var(--navy)" stroke-width="0.9"/><path d="M4 5l3 2.4L10 5" fill="none" stroke="var(--navy)" stroke-width="0.9"/></svg>
    <div class="contact" style="left:38px;">leon@harbourlinepainting.com</div>
    <div class="contact" style="left:208px;">(023) 55 410 410</div>
    <div class="address">48 Shore Road, Terrigal, Australia, 2260</div>
  </div>

  <div class="abs card card-back">
    <span class="brand-name">Harbourline Painting</span>
  </div>

  <div class="abs letterhead">
    <div class="head">
      <span class="brand-name">Harbourline Painting</span>
    </div>
    <div class="foot">48 Shore Road, Terrigal, Australia, 2260 &nbsp;·&nbsp; leon@harbourlinepainting.com &nbsp;·&nbsp; (023) 55 410 410</div>
  </div>

  <section class="abs icon-band">
    <h2 class="abs section-title">ICONS</h2>
    <svg class="abs icon-row" width="1200" height="222" viewBox="0 0 1200 222" role="img" aria-label="Contact icon set: web, chat, email, phone and location, in white and sky blue">
      <defs>
        <g id="icon-web" fill="none" stroke="currentColor" stroke-width="3.5">
          <circle r="25"/>
          <circle r="12" stroke-width="3"/>
          <ellipse rx="5" ry="12" stroke-width="2.5"/>
          <line x1="-12" y1="0" x2="12" y2="0" stroke-width="2.5"/>
        </g>
        <g id="icon-chat" fill="none" stroke="currentColor" stroke-width="3.5">
          <circle r="25"/>
          <path d="M-12 -9h24v15h-14l-6 6v-6h-4z" stroke-width="3" stroke-linejoin="round"/>
        </g>
        <g id="icon-mail" fill="none" stroke="currentColor" stroke-width="3.5">
          <circle r="25"/>
          <rect x="-12" y="-8" width="24" height="16" stroke-width="3"/>
          <path d="M-12 -8l12 9 12-9" stroke-width="3"/>
        </g>
        <g id="icon-phone" fill="none" stroke="currentColor" stroke-width="3.5">
          <circle r="25"/>
          <path d="M-10 -11c0 13 8 21 21 21l2-6-6-3-3 3c-4-2-7-5-9-9l3-3-3-6z" fill="currentColor" stroke="none"/>
        </g>
        <g id="icon-pin" fill="none" stroke="currentColor" stroke-width="3.5">
          <circle r="25"/>
          <path d="M0 14c-7-8-10-13-10-18a10 10 0 0 1 20 0c0 5-3 10-10 18z" stroke-width="3"/>
          <circle cy="-4" r="3.5" fill="currentColor" stroke="none"/>
        </g>
      </defs>
      <g class="icons-white">
        <use href="#icon-web" x="96" y="120"/>
        <use href="#icon-chat" x="188" y="120"/>
        <use href="#icon-mail" x="284" y="120"/>
        <use href="#icon-phone" x="380" y="120"/>
        <use href="#icon-pin" x="477" y="120"/>
      </g>
      <g class="icons-sky">
        <use href="#icon-web" x="586" y="120"/>
        <use href="#icon-chat" x="678" y="120"/>
        <use href="#icon-mail" x="774" y="120"/>
        <use href="#icon-phone" x="871" y="120"/>
        <use href="#icon-pin" x="967" y="120"/>
      </g>
    </svg>
  </section>
</main>
</body>
</html>
```